Tolvane 3D Pen Filaments Refill Packaging design

Hello,
My company is Tolvane which selling eco products, like bamboo towels, palm leaf plates and eco friendly 3d printing filaments. I need an a...

Target Market(s)

Children, 3d printing hobbyists, students and 3d designers

Industry/Entity Type

It Company

```html
<!DOCTYPE html>
<html lang="en">
<head>
<meta charset="utf-8">
<title>3D Pen Filament Refills Header Card</title>
<link rel="stylesheet" href="https://fonts.googleapis.com/css2?family=Montserrat:wght@700&family=Oswald:wght@300&family=Yeseva+One&display=swap">
<style>
  :root {
    --page: #ffffff;
    --band: #2f2f31;
    --gold: #f3c84a;
    --white: #ffffff;
    --strip-blue: #5b7cc4;
    --strip-green: #6fbf4c;
    --hanger: #cfd0d2;
    --hanger-edge: #8d8e90;
  }
  html, body {
    margin: 0;
    padding: 0;
    width: 1200px;
    height: 1200px;
    overflow: hidden;
    background: var(--page);
  }
  .canvas {
    position: relative;
    width: 1200px;
    height: 1200px;
  }
  .header-card {
    position: absolute;
    left: 40px;
    top: 472px;
    width: 1140px;
    height: 256px;
    overflow: hidden;
  }
  .card-pattern {
    position: absolute;
    inset: 0;
    background: linear-gradient(90deg, #c7a6d8 0%, #f2c78f 18%, #b9dc9c 35%, #cfd0d4 50%, #c6b3e0 65%, #a9c4ec 80%, #f3c48c 92%, #b9dc9c 100%);
  }
  .title-band {
    position: absolute;
    left: 200px;
    top: 50px;
    width: 810px;
    height: 150px;
    background: var(--band);
    border-radius: 6px 10px 4px 8px;
  }
  .coil-art {
    position: absolute;
    border-radius: 50%;
  }
  .coil-left {
    left: 36px; top: 26px; width: 210px; height: 210px;
    background: conic-gradient(#e64646, #f18a2e, #f6d93a, #7cd35a, #5bc8e8, #3d55b8, #a548b8, #ea66a6, #9a9a9a, #222, #e64646);
  }
  .coil-right {
    left: 786px; top: 4px; width: 150px; height: 104px;
    background: conic-gradient(#e64646, #f18a2e, #f6d93a, #7cd35a, #5bc8e8, #3d55b8, #a548b8, #ea66a6, #9a9a9a, #e64646);
  }
  .pen-art {
    position: absolute;
    left: 946px; top: 24px; width: 132px; height: 218px;
    background: linear-gradient(135deg, #a3369e 0%, #7a4aa8 50%, #2f55b0 100%);
    border-radius: 14px;
  }
  .hanger-hole {
    position: absolute;
    left: 494px; top: 34px;
    width: 150px; height: 70px;
  }
  .brand-title {
    position: absolute;
    font-family: "Montserrat", sans-serif;
    font-weight: 700;
    color: var(--white);
    margin: 0;
    line-height: 1;
  }
  .title-3d { left: 299px; top: 76px; font-size: 50px; }
  .title-pen { left: 378px; top: 128px; font-size: 54px; }
  .tagline {
    position: absolute;
    left: 536px;
    top: 120px;
    margin: 0;
    font-family: "Yeseva One", serif;
    color: var(--gold);
    font-size: 21px;
    line-height: 30px;
    white-space: nowrap;
  }
  .tagline .count { font-size: 28px; }
  .colour-strip {
    position: absolute;
    left: 312px;
    top: 202px;
    height: 38px;
    display: flex;
    font-family: "Oswald", sans-serif;
    font-weight: 300;
    font-size: 15px;
    color: var(--white);
  }
  .strip-item {
    display: flex;
    align-items: center;
    justify-content: center;
    height: 100%;
    white-space: nowrap;
  }
  .strip-standard { width: 216px; background: var(--strip-blue); border-radius: 4px 0 0 4px; }
  .strip-glow { width: 244px; background: var(--strip-green); }
  .strip-clear { width: 246px; background: var(--strip-blue); border-radius: 0 4px 4px 0; }
</style>
</head>
<body>
<div class="canvas">
  <section class="header-card">
    <div class="card-pattern" role="img" aria-label="Soft multicoloured bokeh dot pattern background"></div>
    <div class="title-band"></div>
    <div class="coil-art coil-left" role="img" aria-label="Ring of coiled multicoloured filament strands"></div>
    <div class="coil-art coil-right" role="img" aria-label="Small ring of coiled multicoloured filament strands"></div>
    <div class="pen-art" role="img" aria-label="Photo of a purple and a blue 3D pen"></div>
    <svg class="hanger-hole" viewBox="0 0 157 74" aria-hidden="true">
      <path d="M20 22 H58 Q60 2 78 2 Q96 2 98 22 H137 Q155 22 155 48 Q155 72 137 72 H20 Q2 72 2 48 Q2 22 20 22 Z" fill="var(--hanger)" stroke="var(--hanger-edge)" stroke-width="2"/>
    </svg>
    <h1 class="brand-title title-3d">3D</h1>
    <p class="brand-title title-pen">PEN</p>
    <p class="tagline">Filament Refills - Pla Pack<br>With <span class="count">20</span> Amazing Colours</p>
    <div class="colour-strip">
      <span class="strip-item strip-standard">14 AMAZING COLOURS</span>
      <span class="strip-item strip-glow">+ 3 MYSTERY GLOW IN DARK COLOURS</span>
      <span class="strip-item strip-clear">+ 3 MAGICAL TRANSPARENT COLOURS</span>
    </div>
  </section>
</div>
</body>
</html>
```